Land Buying Company Needs Letterhead for Direct Mail Marketing to Land Owners

We are looking for a professional letterhead that we will be including in our direct mail marketing. We will be sending this to land owners who may be interested in selling or purchasing land.

The letterhead needs to be editable. Headers and footers would look nice, but we are open. We would want it to include our address, website, phone, and email info. For right now the address to use for design purposes would the following:

Address: 415 Bramwell Avenue #600
Dallas, TX 75219
Website - www.quillridgeacres.example
Email - info@quillridgeacres.example
Phone - 866-402-ACRE

I have attached our logo zip file that we just had done on Pixel Guild. Let me know what questions you have, and thank you.

```html
<!DOCTYPE html>
<html lang="en">
<head>
<meta charset="utf-8">
<title>Quill Ridge Acres — Letterhead</title>
<link rel="stylesheet" href="https://fonts.googleapis.com/css2?family=Arimo:wght@400&family=Montserrat:wght@400;700&display=swap">
<style>
  :root {
    --backdrop: #737373;
    --paper-top: #ffffff;
    --paper-bottom: #ececec;
    --forest: #44601c;
    --leaf: #8dc63f;
    --ink: #4a4a4a;
    --ink-soft: #5a5a5a;
  }
  * { box-sizing: border-box; margin: 0; padding: 0; }
  html, body { width: 1200px; height: 774px; overflow: hidden; }
  body { background: var(--backdrop); position: relative; }

  .sheet {
    position: absolute;
    top: 59px;
    width: 458px;
    height: 647px;
    background: linear-gradient(160deg, var(--paper-top) 0%, var(--paper-bottom) 100%);
    overflow: hidden;
  }
  .sheet--first { left: 169px; }
  .sheet--second { left: 673px; background: #f2f2f2; }

  .brand {
    position: absolute;
    top: 40px;
    left: 0; right: 0;
    display: flex;
    align-items: center;
    justify-content: center;
    gap: 10px;
  }
  .brand__dot { width: 40px; height: 40px; border-radius: 50%; background: var(--forest); }
  .brand__name {
    font-family: "Montserrat", sans-serif;
    font-weight: 700;
    font-size: 21px;
    letter-spacing: 1px;
    color: var(--forest);
  }

  .letter {
    position: absolute;
    left: 41px;
    top: 185px;
    width: 379px;
    font-family: "Arimo", sans-serif;
    color: var(--ink);
  }
  .letter__greeting { font-size: 11.3px; margin-bottom: 18px; }
  .letter__body p {
    font-size: 6.75px;
    line-height: 9.8px;
    text-align: justify;
    margin-bottom: 10px;
    color: var(--ink-soft);
  }
  .letter__closing { font-size: 6.9px; margin-top: 17px; color: var(--ink-soft); }
  .letter__signature {
    width: 138px;
    height: 30px;
    margin-top: 4px;
    background: linear-gradient(90deg, rgba(40,40,40,0.18), rgba(40,40,40,0.06));
    border-radius: 3px;
  }

  .contact {
    position: absolute;
    left: 39px;
    top: 582px;
    list-style: none;
    font-family: "Montserrat", sans-serif;
    font-size: 7.2px;
    color: var(--ink);
  }
  .contact li { display: flex; align-items: flex-start; gap: 5px; line-height: 9.3px; }
  .contact li + li { margin-top: 0.5px; }
  .contact__address { margin-bottom: 1px; }
  .contact svg { width: 6px; height: 6px; margin-top: 1.6px; flex: none; fill: var(--forest); }

  .scenery {
    position: absolute;
    left: 268px;
    top: 538px;
    width: 177px;
    height: 103px;
    background: linear-gradient(180deg, rgba(141,198,63,0.55) 0%, rgba(68,96,28,0.85) 55%, var(--forest) 100%);
    border-radius: 40px 40px 0 0;
  }
  .base-band {
    position: absolute;
    left: 0; right: 0; bottom: 0;
    height: 6px;
    background: var(--forest);
  }
</style>
</head>
<body>

<section class="sheet sheet--first" aria-label="Letterhead page one">
  <header class="brand">
    <span class="brand__dot"></span>
    <span class="brand__name">QUILL RIDGE ACRES</span>
  </header>

  <article class="letter">
    <p class="letter__greeting">Dear Mr. Harlow,</p>
    <div class="letter__body">
      <p>Lorem ipsum dolor sit amet, consectetur adipiscing elit. Donec orci purus, luctus vitae dignissim eu, iaculis sed purus. Vivamus faucibus, ipsum nec aliquet viverra, leo mauris condimentum ligula, sit amet sagittis enim ligula quis arcu. Nam egestas tortor id nisi porttitor mattis. In tortor ante, ultricies in suscipit a, tempus non massa. Vivamus et auctor mi. Fusce vel massa nulla. Phasellus nec eros mauris, et scelerisque orci.</p>
      <p>Donec malesuada orci vitae nulla accumsan porta a id massa. Quisque accumsan iaculis magna sit amet fringilla. Maecenas consequat, magna eget tincidunt semper, odio nibh rutrum mi, id feugiat ante nisi eu risus. Vestibulum nunc orci, rhoncus a placerat in, ultricies in mi. Cras mattis varius eros, vel fringilla nisi suscipit eget. Quisque scelerisque sagittis nulla at porttitor.</p>
      <p>Sed id augue vitae urna euismod commodo aliquet a quam. Pellentesque arcu velit, cursus et malesuada ut, consequat et diam. Nullam erat sem, rhoncus id ullamcorper vitae, rhoncus et arcu. In ultricies ultricies nulla, ut rutrum nisi iaculis at. Donec eu magna a metus ornare faucibus. Fusce aliquet faucibus ultricies. Morbi semper, est id tincidunt gravida, sem arcu adipiscing lacus, ac bibendum nulla leo eu purus. Quisque nec diam sed risus consectetur a ccumsan quis quis nibh. Vestibulum id purus lorem.</p>
      <p>It is a long established fact that a reader will be distracted by the readable content of a page when looking at its layout. The point of using Lorem Ipsum is that it has a more-or-less normal distribution of letters, as opposed to using ‘Content here, content here’, making it look like readable English. Many desktop publishing packages</p>
      <p>ada ut, consequat et diam. Nullam erat sem, rhoncus id ullamcorper vitae, rhoncus et arcu. In ultricies ultricies nulla, ut rutrum nisi iaculis at. Donec eu magna a metus ornare faucibus. Fusce aliquet faucibus ultricies. Morbi semper,</p>
    </div>
    <p class="letter__closing">Sincerely,</p>
    <div class="letter__signature" role="img" aria-label="Handwritten signature"></div>
  </article>

  <ul class="contact">
    <li class="contact__address">
      <svg viewBox="0 0 10 10"><path d="M5 0a3.6 3.6 0 0 0-3.6 3.6C1.4 6.3 5 10 5 10s3.6-3.7 3.6-6.4A3.6 3.6 0 0 0 5 0zm0 5a1.4 1.4 0 1 1 0-2.8A1.4 1.4 0 0 1 5 5z"/></svg>
      <span>415 Bramwell Avenue #600<br>Dallas, TX 75219</span>
    </li>
    <li>
      <svg viewBox="0 0 10 10"><path d="M2.2 0.5l1.6 2.2-1 1.1a6 6 0 0 0 3.4 3.4l1.1-1 2.2 1.6-0.8 1.7C4.6 9.4 0.6 5.4 0.5 1.3z"/></svg>
      <span>866-402-ACRE</span>
    </li>
    <li>
      <svg viewBox="0 0 10 10"><path d="M0 2h10v6H0z M0 2l5 3.4L10 2" fill="none" stroke="#44601c" stroke-width="1.2"/><path d="M0 2h10L5 5.3z"/></svg>
      <span>info@quillridgeacres.example</span>
    </li>
    <li>
      <svg viewBox="0 0 10 10"><circle cx="5" cy="5" r="4.3" fill="none" stroke="#44601c" stroke-width="1.2"/><path d="M3 2.5l2 1-1 2 1.5 1.5-0.5 2L2.5 7 3 5 1.8 3.8z M6.5 1.5l2 2-1.5 1z"/></svg>
      <span>www.quillridgeacres.example</span>
    </li>
  </ul>

  <div class="scenery" role="img" aria-label="Three pine trees with a small green bird flying above"></div>
  <div class="base-band"></div>
</section>

<section class="sheet sheet--second" aria-label="Letterhead page two">
  <div class="scenery" role="img" aria-label="Three pine trees with a small green bird flying above"></div>
  <div class="base-band"></div>
</section>

</body>
</html>
```